Letterhead Design Project

Quillfern Consulting is a newly created boutique consultancy focussing on delivering strategic consulting to medium and large businesses, with a focus on:
- Strategic planning and execution.
- Corporate function optimisation, especially in the areas of finance, commercial, and IT. This includes implementing the right functional design for the needs of the business, and ensuring the right skills.
- Performance management, in particular project governance and control, operational metrics and management reporting.
I have in mind a tag line for the business being:
"Helping business to discover sustainable value."
I am looking for a letterhead design which utilises my new logo on report templates (powerpoint and word), and letterhead.
Lexiborn defines a mother lode as follows:
"Mother lode is a principal vein or zone of veins of gold or silver ore. The term probably came from a literal translation of the Spanish veta madre, a term common in old Mexican mining. Veta madre, for instance, is the name given to an 11-kilometre-long (6.8 mi) silver vein discovered in 1548 in Guanajuato, New Spain (modern-day Mexico)."
My preference is for black and gold. Logo files are attached in .eps format. All fonts are outlined. The fonts that are used are "Crimson Text" and "Josefin Sans". They are free open source fonts and they are available here: http://www.glyphbarn.com/fonts
Target Market(s)
Medium to large corporates.
Industry/Entity Type
Boutique
Other font styles liked:
- All fonts are outlined. The fonts that are used are "Crimson Text" and "Josefin Sans". They are free open source fonts and they are available here: http://www.glyphbarn.com/fonts

```html
<!DOCTYPE html>
<html lang="en">
<head>
<meta charset="utf-8">
<title>Quillfern Consulting – Letterhead</title>
<link rel="stylesheet" href="https://fonts.googleapis.com/css2?family=Crimson+Text:wght@400&family=Josefin+Sans:wght@300&display=swap">
<style>
  :root {
    --ink: #0a0a0a;
    --paper: #ffffff;
    --gold: #d4a20f;
  }
  html, body {
    margin: 0;
    padding: 0;
    overflow: hidden;
    background: var(--ink);
  }
  .letterhead {
    position: relative;
    width: 854px;
    height: 1200px;
    background: var(--ink);
    overflow: hidden;
  }
  .letterhead__sheet {
    position: absolute;
    inset: 0;
    width: 854px;
    height: 1200px;
  }
  .letterhead__sheet .writing-area { fill: var(--paper); }
  .brand {
    position: absolute;
    top: 43px;
    left: 172px;
    display: flex;
    align-items: center;
    gap: 22px;
  }
  .brand__square {
    width: 100px;
    height: 100px;
    box-sizing: border-box;
    border: 6px solid var(--paper);
  }
  .brand__name {
    font-family: "Crimson Text", Georgia, serif;
    font-weight: 400;
    font-size: 46px;
    line-height: 1.1;
    letter-spacing: 0.06em;
    text-transform: uppercase;
    color: var(--paper);
    margin: 0;
  }
  .tagline {
    position: absolute;
    left: 0;
    right: 0;
    top: 1148px;
    margin: 0;
    text-align: center;
    font-family: "Crimson Text", Georgia, serif;
    font-weight: 400;
    font-size: 13px;
    letter-spacing: 0.16em;
    text-transform: uppercase;
    color: var(--paper);
  }
</style>
</head>
<body>
  <div class="letterhead">
    <svg class="letterhead__sheet" viewBox="0 0 854 1200" aria-hidden="true">
      <path class="writing-area"
            d="M0,218 C300,160 650,290 854,540 L854,1062 C700,940 300,880 0,1000 Z"/>
    </svg>

    <header class="brand">
      <div class="brand__square"></div>
      <h1 class="brand__name">Quillfern Consulting</h1>
    </header>

    <p class="tagline">Helping business discover sustainable value</p>
  </div>
</body>
</html>
```